E-Commerce Website Update for Bamboo Poles Company

Existing website at:

http://www.reedcraftstudio.example/
http://www.reedcraftstudio.example/pages/product-and-price-list

Two pages to design: home page and "price list" page.

Info for home page as follows:

HOME PAGE:

Header:
Company Name: reedcraft studio
Telephone: 1 888 412 5093

Across the top:
Home | Price List | Blog | FAQ | About | Contact

Down the side:
About Bamboo
Wedding Arbors
Bamboo For Flutes
Black Bamboo
Spotted Bamboo
Bamboo Carpentry
Photo Gallery
All Products & Prices
Blog
FAQ
About
Contact

Should have shopping cart and search buttons on top.
Please see ai file, attached for logo (leaf) and font
In addition the homepage should have one or two sections for promotions

Chosen design will be asked to help deign a PRODUCT AND PRICE LIST page similar to the one we have now, but with "LEARN MORE" and "ORDER NOW" buttons for each item.
Updates

Reason: Thanks  for all the designs so far; giving an extra week for extra consideration.

Target Market(s)

Consumers, wedding planners.

Industry/Entity Type

Shopping

Requirements
Must have
• Clean, easy to read design.
Should not have
• No flash animation.

```html
<!DOCTYPE html>
<html lang="en">
<head>
<meta charset="utf-8">
<title>reedcraft studio — Pole Provider</title>
<link rel="stylesheet" href="https://fonts.googleapis.com/css2?family=Arimo:wght@400;700&family=Open+Sans:wght@400&display=swap">
<style>
:root{
  --ink:#1c1c1c;
  --text:#6b6b6b;
  --green:#6a9a2c;
  --topbar:#0d0d0d;
  --wood:#8b6a4e;
  --wood-dark:#74553c;
  --hero-bg:#e6e3e1;
  --footer:#2d2d2d;
  --footer-text:#c9c9c9;
  --white:#ffffff;
}
*{box-sizing:border-box;margin:0;padding:0}
html,body{width:963px;height:1200px;overflow:hidden;background:var(--white)}
body{position:relative;font-family:Arimo,Arial,sans-serif;color:var(--text)}
a{color:inherit;text-decoration:none}
.abs{position:absolute}

/* top bar */
.topbar{left:0;top:0;width:963px;height:26px;background:var(--topbar);color:#e8e8e8;font-size:11.5px}
.topbar .phone{left:18px;top:7px;color:#bdbdbd}
.topbar .account{left:184px;top:8px;text-decoration:underline}
.topbar .wishlist{left:253px;top:8px}
.topbar .bag{left:318px;top:6px;display:flex;gap:6px;align-items:center}
.topbar .bag b{font-weight:700}
.topbar .currency-label{left:511px;top:7px}
.topbar .currency{left:589px;top:6px;width:86px;height:15px;background:#dcdcdc;color:#777;font-size:10px;padding:1px 4px}
.topbar .currency span{position:absolute;right:2px;top:2px;width:14px;height:11px;background:#888}
.topbar .search-field{left:695px;top:5px;width:137px;height:17px;background:#fff}
.topbar .search-btn{left:832px;top:5px;width:63px;height:17px;background:#8c8c8c;color:#fff;font-size:11.5px;text-align:center;line-height:17px}

/* header */
.header{left:0;top:26px;width:963px;height:75px;background:linear-gradient(180deg,var(--wood),var(--wood-dark));border-bottom:3px solid #cbb79f}
.logo{left:52px;top:12px;font-size:28px;line-height:25px;color:#2a1d12;letter-spacing:-.5px}
.nav{left:183px;top:56px;display:flex;font-size:13px;font-weight:700;color:#fff}
.nav a{padding:0 18px}
.nav a:first-child{padding-left:0}
.nav a+a{border-left:1px solid #b89d83}
.checkout{left:677px;top:45px;width:99px;height:25px;border-radius:12px;background:linear-gradient(#fff,#e3e3e3);color:#222;font-size:12px;text-align:center;line-height:25px}
.leaf{left:865px;top:26px;width:98px;height:78px;background:linear-gradient(200deg,rgba(88,150,30,.55),rgba(88,150,30,0) 70%)}

/* hero */
.hero{left:0;top:104px;width:963px;height:530px;background:var(--hero-bg)}
.gallery{left:44px;top:125px;width:599px;height:470px;background:var(--green);border-radius:4px}
.photo-main{left:7px;top:7px;width:439px;height:458px;background:linear-gradient(180deg,#c8d2dc,#b19a74)}
.thumb{left:456px;width:137px;height:147px;background:linear-gradient(180deg,#d6c99a,#a99254)}
.welcome{left:675px;top:133px;width:255px}
.welcome h1{font-size:21px;line-height:24px;color:var(--ink);font-weight:700;letter-spacing:.3px}
.welcome p{margin-top:15px;font-size:11px;line-height:17.3px;color:var(--text)}
.read-more{display:inline-block;margin-top:9px;background:var(--green);color:#fff;font-size:9.5px;padding:3px 4px;letter-spacing:.5px}
.side-nav{left:677px;top:392px;list-style:none;font-size:12px;font-weight:700;color:#7a7a7a}
.side-nav li{height:27.8px;padding-left:10px;position:relative;letter-spacing:.3px}
.side-nav li::before{content:"";position:absolute;left:0;top:3px;border-left:5px solid #111;border-top:4px solid transparent;border-bottom:4px solid transparent}
.side-nav li:first-child{color:var(--ink)}

/* section titles */
.section-title{font-size:26px;color:var(--ink);line-height:28px;font-weight:400}
.section-title small{display:block;font-size:16px;line-height:24px;font-weight:400}
.featured-title{left:44px;top:662px}

/* products */
.product{top:729px;width:190px}
.product .frame{width:151px;height:159px;background:var(--green);border-radius:4px;padding:6px}
.product .frame div{width:100%;height:100%}
.product h3{margin-top:23px;font-size:12.5px;font-weight:700;color:var(--green);letter-spacing:-.2px}
.product .size{font-size:10.5px;color:var(--green);margin-top:2px}
.product p{margin-top:17px;font-size:11px;line-height:14px;width:172px}
.product .buy{position:absolute;top:296px;left:0;display:flex;align-items:center;gap:7px;font-size:12.5px;font-weight:700;color:var(--ink)}
.product .buy a{background:var(--green);color:#fff;width:62px;height:24px;line-height:24px;text-align:center;font-size:12.5px}

/* news */
.news-title{left:677px;top:664px}
.rss{left:879px;top:668px;display:flex;align-items:center;gap:3px;font-size:15px;color:#e0b89a;font-family:Georgia,serif}
.news{left:677px;top:721px;width:250px;font-size:11px;line-height:13.5px;letter-spacing:.2px}
.news .date{color:var(--ink);font-size:11px}
.news article{margin-bottom:14px}
.newsletter-title{left:680px;top:944px;font-size:31px;line-height:32px}
.newsletter-note{left:676px;top:1004px;font-size:11px;letter-spacing:.2px}
.newsletter-field{left:676px;top:1033px;width:183px;height:19px;border:1px solid #ccc}
.signup{left:864px;top:1030px;width:62px;height:24px;background:var(--green);color:#fff;font-size:12.5px;font-weight:700;text-align:center;line-height:24px}

/* footer */
.footer{left:0;top:1077px;width:963px;height:123px;background:var(--footer);border-top:5px solid #c8c0b8}
.footer-logo{left:48px;top:22px;font-size:28px;line-height:25px;color:#f2f2f2}
.copyright{left:48px;top:86px;font-family:"Open Sans",Arial,sans-serif;font-size:12.5px;color:var(--footer-text)}
.footer-links{right:35px;top:86px;display:flex;gap:13px;font-family:"Open Sans",Arial,sans-serif;font-size:12.5px;color:var(--footer-text)}
.footer-links a:first-child{text-decoration:underline}
.social{right:32px;top:22px;display:flex;gap:19px}
.social a{display:flex;flex-direction:column;align-items:center;gap:2px;font-size:8px;color:var(--footer-text);width:36px}
.social span{width:31px;height:31px;background:#6f6f6f;border-radius:3px}
</style>
</head>
<body>

<div class="abs topbar">
  <span class="abs phone">1 888 412 5093</span>
  <a class="abs account" href="#">My Account</a>
  <a class="abs wishlist" href="#">Wishlist</a>
  <div class="abs bag">
    <svg width="14" height="15" viewBox="0 0 14 15"><path d="M2 5h10l1 10H1z" fill="#eee"/><path d="M4.5 5V3.5a2.5 2.5 0 0 1 5 0V5" fill="none" stroke="#eee" stroke-width="1.3"/></svg>
    <span><b>Your Bag</b> 4 items £154.80</span>
  </div>
  <span class="abs currency-label">Currencies:</span>
  <div class="abs currency">US Dollar<span></span></div>
  <div class="abs search-field"></div>
  <a class="abs search-btn" href="#">Search</a>
</div>

<header class="abs header">
  <div class="abs logo">reedcraft<br>studio</div>
  <nav class="abs nav">
    <a href="#">Home</a><a href="#">Price List</a><a href="#">Blog</a><a href="#">FAQ</a><a href="#">About</a><a href="#">Contact</a>
  </nav>
  <a class="abs checkout" href="#">Checkout</a>
  <svg class="abs" style="left:780px;top:32px" width="56" height="44" viewBox="0 0 56 44">
    <path d="M2 10l10 4" stroke="#c33" stroke-width="3"/>
    <path d="M12 14h38l-6 16H17z" fill="#d9d9d9" stroke="#999" stroke-width="1.5"/>
    <path d="M17 30l-2 5h30" fill="none" stroke="#999" stroke-width="1.5"/>
    <circle cx="19" cy="39" r="3" fill="#555"/><circle cx="41" cy="39" r="3" fill="#555"/>
  </svg>
</header>
<div class="abs leaf" role="img" aria-label="Bamboo leaf decoration"></div>

<section class="abs hero"></section>
<div class="abs gallery">
  <div class="abs photo-main" role="img" aria-label="Tall stacks of bamboo poles drying outdoors"></div>
  <div class="abs thumb" style="top:7px" role="img" aria-label="Bamboo poles stacked in a warehouse"></div>
  <div class="abs thumb" style="top:162px" role="img" aria-label="Ends of stacked bamboo poles"></div>
  <div class="abs thumb" style="top:318px" role="img" aria-label="Stacked bamboo poles close-up"></div>
</div>

<div class="abs welcome">
  <h1>Welcome to your<br>Pole Provider</h1>
  <p>Need bamboo poles at a competitive price? Welcome to your one-stop pole shop.We warehouse a variety of types poles in a variety of diameters, from 5/8" to 5 1/2", in lengths up to 8'. We have natural poles, moso (mao) timber poles, black poles spotted poles… and regular bamboo poles. Whatever your project may be, from flutes to weddings to roasting a pig, we have the perfect pole for you.</p>
  <a class="read-more" href="#">Read More</a>
</div>

<ul class="abs side-nav">
  <li>About Bamboo</li>
  <li>Wedding Arbors</li>
  <li>Bamboo For Flutes</li>
  <li>Black Bamboo</li>
  <li>Spotted Bamboo</li>
  <li>Bamboo Carpentry</li>
  <li>Photo Gallery</li>
  <li>All Products &amp; Prices</li>
</ul>

<h2 class="abs section-title featured-title">Featured<small>products</small></h2>

<div class="abs product" style="left:44px">
  <div class="frame"><div role="img" aria-label="Mao bamboo poles" style="background:#e2d6a6"></div></div>
  <h3>MAO BAMBOO POLES</h3>
  <div class="size">5 " x 8'</div>
  <p>Carton of 2 timber-type Chinese Mao Bamboo Poles. 5" diameter x 8 feet length. Dried and treated, imported from China.</p>
  <div class="buy">Price: $40.00 <a href="#">Buy it</a></div>
</div>

<div class="abs product" style="left:255px">
  <div class="frame"><div role="img" aria-label="Black bamboo poles" style="background:#ececec"></div></div>
  <h3>BLACK BAMBOO POLES</h3>
  <div class="size">15 pcs 1" x 8 feet</div>
  <p>Carton of 15 dried and treated Black Bamboo poles (species phyllostachys nigra).</p>
  <div class="buy">Price: $53.25 <a href="#">Buy it</a></div>
</div>

<div class="abs product" style="left:469px">
  <div class="frame"><div role="img" aria-label="Nan bamboo poles" style="background:#e0d9a6"></div></div>
  <h3>NAN BAMBOO POLES</h3>
  <div class="size">4 pcs 2" x 8'</div>
  <p>Carton of 4 Chinese Nan Bamboo Poles. 2" diameter x 8 feet length. Dried and treated, imported from China.</p>
  <div class="buy">Price: $24.00 <a href="#">Buy it</a></div>
</div>

<h2 class="abs section-title news-title">Latest<small>news</small></h2>
<div class="abs rss">
  <svg width="20" height="20" viewBox="0 0 20 20"><circle cx="4" cy="16" r="3" fill="#e7c4a8"/><path d="M2 8a10 10 0 0 1 10 10M2 2a16 16 0 0 1 16 16" fill="none" stroke="#e7c4a8" stroke-width="2.6"/></svg>rss
</div>
<div class="abs news">
  <article><div class="date">05.02.11</div>Carton of 2 timber-type Chinese Mao Bamboo Poles. 5" diameter x 8 feet length. Dried and treated, imported from China.</article>
  <article><div class="date">05.02.11</div>Carton of 2 timber-type Chinese Mao Bamboo Poles. 5" diameter x 8 feet length. Dried and treated, imported from China.</article>
  <article><div class="date">05.02.11</div>Carton of 2 timber-type Chinese Mao Bamboo Poles. 5" diameter x 8 feet length. Dried and treated, imported from China.</article>
</div>

<h2 class="abs section-title newsletter-title">Newsletter<small style="margin-top:4px">sign&nbsp; up</small></h2>
<p class="abs newsletter-note">Info sales, promotions and events at the shop</p>
<div class="abs newsletter-field"></div>
<a class="abs signup" href="#">sign up</a>

<footer class="abs footer">
  <div class="abs footer-logo">reedcraft<br>studio</div>
  <div class="abs social">
    <a href="#"><span></span>Chirpline</a>
    <a href="#"><span></span>Friendwall</a>
    <a href="#"><span></span>Bidmarket</a>
    <a href="#"><span></span>Vidstream</a>
  </div>
  <p class="abs copyright">Copyright © 2011 Online Shop, All Rights Reserved</p>
  <nav class="abs footer-links">
    <a href="#">Privacy Policy</a><a href="#">T&amp;Cs</a><a href="#">Accessibility</a><a href="#">Responsibilities</a><a href="#">About Us</a><a href="#">Careers</a><a href="#">FAQs</a><a href="#">Contact us</a>
  </nav>
</footer>

</body>
</html>
```